Webdesign für Gebäudereinigung
Zielgruppe
Seit 2005 ist LUM Dienstleistungen der Partner für Gebäudereinigung in Berlin. Wir haben Firmenkunden sowie privat Kunden und kümmern uns um sämtliche Reinigungen. Wie Glasreinigung, Büro- und Unterhaltungsreinigung, Bau- und Baufeinreinigung, Aufgangsreinigung & Grundreinigung…
Aufgabenstellung
Unsere neue Webseite sollte modern - Zeitlos - freundlich sein … Farben am Logo orientieren, das übernehmen wir weiterhin….

```html
<!DOCTYPE html>
<html lang="de">
<head>
<meta charset="utf-8">
<title>LUM Dienstleistungen – Gebäudereinigung in Berlin</title>
<link href="https://fonts.googleapis.com/css2?family=Poppins:wght@300;400;500;600&display=swap" rel="stylesheet">
<style>
:root{
  --brand:#2f4f86;
  --brand-dark:#2c4a7e;
  --text:#2f4f86;
  --muted:#5a6f99;
  --white:#ffffff;
  --line:#9fb0cf;
  --panel:rgba(255,255,255,0.78);
}
*{box-sizing:border-box;margin:0;padding:0}
html,body{width:1200px;height:3041px;overflow:hidden;background:var(--white)}
body{font-family:"Poppins",sans-serif;color:var(--text);position:relative}
.abs{position:absolute}

/* header */
.site-header{position:absolute;left:0;top:0;width:1200px;height:153px}
.brand{position:absolute;left:87px;top:0;display:flex;align-items:flex-end;height:130px}
.brand-square{width:108px;height:130px;background:var(--brand)}
.brand-name{font-size:23px;font-weight:400;color:var(--brand);margin-left:8px;margin-bottom:4px;white-space:nowrap}
.topbar{position:absolute;right:87px;top:20px;display:flex;align-items:center;gap:14px;font-size:16px;font-weight:300}
.topbar .dot{width:16px;height:16px;background:var(--brand);border-radius:3px}
.main-nav,.footer-nav{display:flex;gap:22px;font-size:15.5px;font-weight:400;letter-spacing:.2px}
.main-nav{position:absolute;right:87px;top:110px}

/* hero */
.hero{position:absolute;left:0;top:153px;width:1200px;height:421px;
  background:linear-gradient(100deg,#e9edf1 0%,#f6f7f8 35%,#dfe6ea 60%,#b9c9c4 80%,#d6e0e3 100%)}
.hero-panel{position:absolute;left:0;top:84px;width:744px;height:252px;background:var(--panel);padding:28px 40px 0 87px}
.hero-panel h1{font-size:29px;font-weight:600;line-height:1.2}
.hero-panel .lead{font-size:16px;font-weight:300;margin-top:2px}
.hero-panel p.body{font-size:12.5px;font-weight:300;line-height:21px;margin-top:12px}

/* partners */
.partners{position:absolute;left:0;top:600px;width:1200px;text-align:center}
.partners h2{font-size:28px;font-weight:500}
.partner-row{display:flex;justify-content:center;gap:70px;margin-top:30px}
.badge{height:56px;background:#d3dbe8;border-radius:4px}

/* feature rows */
.feature{position:absolute;left:0;width:1200px;height:400px}
.feature .photo{position:absolute;top:0;width:600px;height:400px}
.feature .copy{position:absolute;top:0;width:500px}
.feature h3{font-size:28px;font-weight:500;line-height:1.2}
.feature p{font-size:16.3px;font-weight:300;line-height:26.2px;margin-top:30px}

/* contact */
.contact-head{position:absolute;left:87px;top:2153px;border-left:17px solid var(--brand);padding-left:17px;height:57px}
.contact-head h2{font-size:39px;font-weight:500;line-height:1;margin-top:-4px}
.contact-head p{font-size:16px;font-weight:300;margin-top:2px;color:#333}
.contact-form{position:absolute;left:87px;top:2277px;width:432px}
.contact-form label{display:block;font-size:13px;font-weight:300;color:#333;margin-bottom:4px}
.field{width:432px;height:30px;border:1px solid var(--line);margin-bottom:25px}
.field.area{height:95px;margin-bottom:16px}
.send{width:123px;height:29px;background:var(--brand);color:#fff;font-size:12px;display:flex;align-items:center;justify-content:center}
.contact-info{position:absolute;left:602px;top:2296px;font-size:16.3px;font-weight:300;color:#333}
.info-line{display:flex;align-items:flex-start;min-height:34px;line-height:34px}
.info-line svg{width:22px;height:22px;margin:6px 14px 0 0;flex:none}
.info-line .indent{margin-left:36px}

/* footer */
.site-footer{position:absolute;left:0;top:2710px;width:1200px;height:331px;background:var(--brand-dark);color:#fff}
.footer-brand{position:absolute;left:87px;top:40px;font-size:22px;font-weight:400}
.footer-brand b{font-weight:600;font-size:24px}
.footer-nav{position:absolute;right:87px;top:56px}
.footer-info{position:absolute;left:87px;top:101px;font-size:16px;font-weight:300;line-height:24px}
.footer-info .info-line{min-height:33px;line-height:24px}
.footer-info svg{margin:2px 14px 0 0}
</style>
</head>
<body>

<header class="site-header">
  <div class="brand"><div class="brand-square"></div><span class="brand-name">LUM Dienstleistungen</span></div>
  <div class="topbar">
    <span class="dot"></span><span class="dot" style="border-radius:50%"></span>
    <svg width="20" height="15" viewBox="0 0 20 15" fill="none" stroke="#2f4f86" stroke-width="1.8"><rect x="1" y="1" width="18" height="13"/><path d="M1 1l9 7 9-7"/></svg>
    <svg width="18" height="18" viewBox="0 0 24 24" fill="none" stroke="#2f4f86" stroke-width="1.8"><path d="M5 3h4l2 5-3 2a11 11 0 0 0 6 6l2-3 5 2v4a2 2 0 0 1-2 2A18 18 0 0 1 3 5a2 2 0 0 1 2-2z"/></svg>
    <span>030 512 604 20</span>
  </div>
  <nav class="main-nav"><span>START</span><span>LEISTUNGEN</span><span>KONTAKT</span><span>DATENSCHUTZ</span><span>IMPRESSUM</span></nav>
</header>

<section class="hero" role="img" aria-label="Helle, moderne Eingangshalle mit Glasfronten und weißen Säulen">
  <div class="hero-panel">
    <h1>L.U.M. Gebäudereinigung in Berlin</h1>
    <p class="lead">Ihre kompetenter Partner für die Objektreinigung.</p>
    <p class="body">L.U.M. Gebäudereinigung in Berlin existiert bereits seit 2005 und ist Mitglied der regionalen Wirtschaftskammer. Unser Team umfasst derzeit rund 20 Mitarbeiterinnen und Mitarbeiter, die sich allesamt durch fachliches Know-how und eine hohe Motivation auszeichnen. LUM Dienstleistungen Berlin ist an langfristigen Partnerschaften interessiert und steht für Werte. Was uns auszeichnet sind Flexibilität, Zuverlässigkeit und Gründlichkeit. Doch der Reihe nach:</p>
  </div>
</section>

<section class="partners">
  <h2>Our Partners</h2>
  <div class="partner-row">
    <div class="badge" style="width:176px"></div>
    <div class="badge" style="width:240px"></div>
    <div class="badge" style="width:316px"></div>
  </div>
</section>

<section class="feature" style="top:830px">
  <div class="photo" style="left:0;background:linear-gradient(180deg,#e6dcc9,#b8ad99 55%,#5f7fb8)" role="img" aria-label="Hotelflur mit Reinigungswagen und abgedecktem blauen Teppich"></div>
  <div class="copy" style="left:627px;top:22px">
    <h3>Flexibil &amp; pünktlich</h3>
    <p>Flexibilität bedeutet im Bereich der Gebäude- und Aufgangsreinigung, dass wir problemlos auch kurzfristige Aufträge übernehmen. Rufen Sie uns an und wir sind meist in kurzer Zeit mit einem Team vor Ort. Gerne übernehmen wir auch die Urlaubsvertretung für eine fest angestellte Fachkraft und arbeiten auf Wunsch auch für Subunternehmen. Flexibilität bedeutet jedoch auch, dass wir gleichermaßen große wie kleine Objekte betreuen. Unabhängig davon, ob Sie einen Partner für ein einzelnes Mehrfamilienhaus oder einen großen Bürokomplex in Berlin suchen: wir unterbreiten Ihnen gerne ein faires Angebot.</p>
  </div>
</section>

<section class="feature" style="top:1231px">
  <div class="copy" style="left:87px;top:18px;width:486px">
    <h3>Kundig &amp; zuverlässig</h3>
    <p style="margin-top:22px">Einer der wichtigsten Punkte unserer Arbeit ist die Zuverlässigkeit. Unabhängig davon, ob Sie mit uns in der Aufgangsreinigung, Büro- und Unterhaltsreinigung oder im Bereich Bau- und Baufeinreinigung zusammen arbeiten können Sie sich auf eine fristgerechte Ausführung aller gewünschten Tätigkeiten verlassen. Anders ausgedrückt: wir halten Wort, sowohl, was den Umfang unserer Arbeit als auch den Zeitpunkt der Ausführung angeht. Möglich wird diese Verlässlichkeit aufgrund unserer langjährigen Erfahrung und unserer flexiblen Teamplanung, die uns immer auch spontane Einsätze in Berlin und Umgebung ermöglicht.</p>
  </div>
  <div class="photo" style="left:600px;background:linear-gradient(160deg,#e8e4d4,#b7b57a 45%,#4a4430 80%,#2b2a20)" role="img" aria-label="Geschwungenes Treppenhaus mit schmiedeeisernem Geländer und gefliesten Wänden"></div>
</section>

<section class="feature" style="top:1631px">
  <div class="photo" style="left:0;background:linear-gradient(90deg,#c9b7a4,#e7e3df 45%,#f2f4f6 70%,#d9dee4)" role="img" aria-label="Helles Büro mit Glaswänden und farbigen Gemälden"></div>
  <div class="copy" style="left:627px;top:20px;width:490px">
    <h3>Kundig &amp; zuverlässig</h3>
    <p style="margin-top:30px">Wenn es um die Reinigung von Wohn- oder Büroflächen, Schwimmbädern, Kitas oder Schulen in Berlin geht, ist Gründlichkeit das A und O. LUM Dienstleistungen führt die Aufträge einerseits schnell, vor allem aber gewissenhaft und mit penibler Sauberkeit aus. Hygiene ist ein integraler Bestandteil unserer Arbeitsweise und zeigt sich auch durch die Verwendung hochwertiger Reinigungsmaterialien und umweltschonender Reinigungsmittel. Wir wissen, dass die Sauberkeit eines Gebäudes gleichzeitig als „Visitenkarte“ der Bewohner oder des dort ansässigen Unternehmens fungiert und tragen dem in verantwortungsvoller Weise Rechnung. Verlassen Sie sich auf uns.</p>
  </div>
</section>

<div class="contact-head">
  <h2>Kontaktieren Sie uns</h2>
  <p>Rufen Sie uns an oder fordern Sie einen Rückruf an:</p>
</div>

<form class="contact-form">
  <label>Ihr Name (Pflichtfeld)</label><div class="field"></div>
  <label>Ihre E-Mail-Adresse (Pflichtfeld)</label><div class="field"></div>
  <label>Betreff</label><div class="field"></div>
  <label>Ihre Nachricht</label><div class="field area"></div>
  <div class="send">SENDEN</div>
</form>

<div class="contact-info">
  <div class="info-line"><svg viewBox="0 0 24 24" fill="none" stroke="#222" stroke-width="1.8"><path d="M12 22s7-7 7-12a7 7 0 0 0-14 0c0 5 7 12 7 12z"/><circle cx="12" cy="10" r="2.5"/></svg>Milan Kovač</div>
  <div class="info-line"><span class="indent">L.U.M. Dienstleistungen</span></div>
  <div class="info-line"><span class="indent">Lindenhof-Str. 14</span></div>
  <div class="info-line"><span class="indent">10719 Berlin</span></div>
  <div class="info-line"><svg viewBox="0 0 24 24" fill="none" stroke="#222" stroke-width="1.8"><path d="M5 3h4l2 5-3 2a11 11 0 0 0 6 6l2-3 5 2v4a2 2 0 0 1-2 2A18 18 0 0 1 3 5a2 2 0 0 1 2-2z"/></svg>030 512 604 20</div>
  <div class="info-line"><svg viewBox="0 0 24 24" fill="#222"><rect x="3" y="8" width="18" height="14" rx="1"/><rect x="7" y="2" width="10" height="7" fill="#222"/><rect x="9" y="12" width="2" height="2" fill="#fff"/><rect x="13" y="12" width="2" height="2" fill="#fff"/><rect x="9" y="16" width="2" height="2" fill="#fff"/><rect x="13" y="16" width="2" height="2" fill="#fff"/></svg>030 512 604 21</div>
  <div class="info-line"><svg viewBox="0 0 24 24" fill="none" stroke="#222" stroke-width="1.8"><rect x="2" y="5" width="20" height="14"/><path d="M2 5l10 8 10-8"/></svg>info@gebaeudereinigung-lum.de</div>
</div>

<footer class="site-footer">
  <div class="footer-brand"><b>LUM</b> Dienstleistungen</div>
  <nav class="footer-nav"><span>START</span><span>LEISTUNGEN</span><span>KONTAKT</span><span>DATENSCHUTZ</span><span>IMPRESSUM</span></nav>
  <div class="footer-info">
    <div class="info-line" style="min-height:103px"><svg viewBox="0 0 24 24" width="22" height="22" fill="none" stroke="#fff" stroke-width="1.8"><path d="M12 22s7-7 7-12a7 7 0 0 0-14 0c0 5 7 12 7 12z"/><circle cx="12" cy="10" r="2.5"/></svg><div>Milan Kovač<br>L.U.M. Dienstleistungen<br>Lindenhof-Str. 14<br>10719 Berlin</div></div>
    <div class="info-line"><svg viewBox="0 0 24 24" width="22" height="22" fill="none" stroke="#fff" stroke-width="1.8"><path d="M5 3h4l2 5-3 2a11 11 0 0 0 6 6l2-3 5 2v4a2 2 0 0 1-2 2A18 18 0 0 1 3 5a2 2 0 0 1 2-2z"/></svg>030 512 604 20</div>
    <div class="info-line"><svg viewBox="0 0 24 24" width="22" height="22" fill="#fff"><rect x="3" y="8" width="18" height="14" rx="1"/><rect x="7" y="2" width="10" height="7"/><rect x="9" y="12" width="2" height="2" fill="#2c4a7e"/><rect x="13" y="12" width="2" height="2" fill="#2c4a7e"/><rect x="9" y="16" width="2" height="2" fill="#2c4a7e"/><rect x="13" y="16" width="2" height="2" fill="#2c4a7e"/></svg>030 512 604 21</div>
    <div class="info-line"><svg viewBox="0 0 24 24" width="22" height="22" fill="none" stroke="#fff" stroke-width="1.8"><rect x="2" y="5" width="20" height="14"/><path d="M2 5l10 8 10-8"/></svg>info@gebaeudereinigung-lum.de</div>
  </div>
</footer>

</body>
</html>
```